Business Card Design for Kind Helper

I am starting my own consultancy business, using what I learned in marketing and advertising to help Non -profits with marketing and communications needs. I need a professional business card design to hand out to my clients.

My business name is “Outreach2Kindness” my vision is that this need this to be reflective of marketing doing good for the world through the power of communications. I like the color palettes in olives, creams and oranges but am open to design options.
In addition to the cards I am asking for separate file for the logo and will need a JPG, PSD Vector File.

Information to go on the card:

Morwenna Calloway
Marketing Consultant
Email: outreach2kindness@mailbrook.com, callowaym1@brinmoreu.edu
Website: Outreach2Kindness.com

Communications

```html
<!DOCTYPE html>
<html lang="en">
<head>
<meta charset="utf-8">
<title>Outreach2Kindness – Business Card</title>
<link rel="stylesheet" href="https://fonts.googleapis.com/css2?family=Arimo:wght@700&family=Didact+Gothic&display=swap">
<style>
  :root {
    --cream: #f8f3d9;
    --olive: #a1a157;
    --olive-text: #a0a057;
    --slate: #7a8a94;
    --white: #ffffff;
  }
  * { margin: 0; padding: 0; box-sizing: border-box; }
  html, body { width: 686px; height: 1200px; overflow: hidden; background: var(--white); }
  .card { position: relative; width: 686px; height: 1200px; background: var(--white); }

  .brand-band {
    position: absolute; top: 0; left: 0; width: 686px; height: 261px;
    background: var(--cream);
    display: flex; flex-direction: column; align-items: center; justify-content: center;
    font-family: "Arimo", Arial, sans-serif; font-weight: 700;
    color: var(--olive-text); font-size: 60px; line-height: 64px; text-align: center;
    letter-spacing: 1px; padding-bottom: 10px;
  }

  .brand-mark { position: absolute; top: 287px; left: 194px; }
  .brand-mark-name {
    position: absolute; top: 604px; left: 0; width: 686px; text-align: center;
    font-family: "Didact Gothic", "Century Gothic", sans-serif;
    font-size: 22px; color: var(--slate);
  }

  .contact-band {
    position: absolute; top: 665px; left: 0; width: 686px; height: 535px;
    background: var(--olive); color: var(--white);
    font-family: "Didact Gothic", "Century Gothic", sans-serif;
  }
  .person-name {
    position: absolute; top: 20px; left: 25px;
    font-family: "Arimo", Arial, sans-serif; font-weight: 700; font-size: 52px; line-height: 60px;
  }
  .person-role { position: absolute; top: 80px; left: 25px; font-size: 34px; line-height: 40px; }
  .mail-icon { position: absolute; top: 236px; left: 314px; }
  .emails {
    position: absolute; top: 272px; left: 0; width: 686px; text-align: center;
    font-size: 33px; line-height: 48px;
  }
  .website {
    position: absolute; top: 474px; left: 0; width: 686px; text-align: center;
    font-size: 37px; line-height: 44px;
  }
</style>
</head>
<body>
  <main class="card">
    <header class="brand-band">
      <span>OUTREACH</span>
      <span>2</span>
      <span>KINDNESS</span>
    </header>

    <svg class="brand-mark" width="298" height="298" viewBox="0 0 298 298" aria-hidden="true">
      <circle cx="149" cy="149" r="143" fill="var(--olive)" stroke="var(--slate)" stroke-width="11"/>
    </svg>
    <p class="brand-mark-name">Outreach2Kindness</p>

    <section class="contact-band">
      <h1 class="person-name">Morwenna Calloway</h1>
      <p class="person-role">Marketing Consultant</p>

      <svg class="mail-icon" width="58" height="30" viewBox="0 0 58 30" aria-hidden="true">
        <rect x="1" y="1" width="56" height="28" fill="none" stroke="var(--white)" stroke-width="1.5"/>
        <polyline points="1,1 29,18 57,1" fill="none" stroke="var(--white)" stroke-width="1.5"/>
        <line x1="1" y1="29" x2="22" y2="14" stroke="var(--white)" stroke-width="1.5"/>
        <line x1="57" y1="29" x2="36" y2="14" stroke="var(--white)" stroke-width="1.5"/>
      </svg>

      <p class="emails">
        outreach2kindness@mailbrook.com<br>
        callowaym1@brinmoreu.edu
      </p>

      <p class="website">Outreach2Kindness.com</p>
    </section>
  </main>
</body>
</html>
```